Broschüre in Querformat für Immobilienmakler
Zielgruppe
Immobilienmakler - Überregional tätig - zielgerichtete Vermarktung - Zielgruppe sind Verkäufer oft ältere Menschen
Ich möchte eine Broschüre mit 12 Seiten im Querformat - Die Broschüre sollte der Website harvrenk-immobilien.example ein wenig ähneln.
Aufgabenstellung
klare Linie - schnell erklärbar und übersichtlich - logischer Aufbau - Aufmerksamkeit erwecken durch Bilder - schnelle Info für Querleser - VERTRAUEN - ehrlich und authentisch - nicht Eitel - schnelle Zurechtfindung - Serviceorientiert - Rundumsorglos Paket

```html
<!DOCTYPE html>
<html lang="de">
<head>
<meta charset="utf-8">
<title>Broschüre – Seiten 08 und 09</title>
<link rel="stylesheet" href="https://fonts.googleapis.com/css2?family=Open+Sans:wght@400;600&display=swap">
<style>
  :root {
    --bg: #dcdcdd;
    --paper: #ffffff;
    --blue-dark: #1c66a8;
    --blue-mid: #2b82c4;
    --blue-light: #63b3e0;
    --heading: #2475b8;
    --text: #6b6b6b;
    --skyline-dark: #7d7f83;
    --skyline-light: #e6e7e9;
  }
  * { box-sizing: border-box; margin: 0; padding: 0; }
  html, body { width: 1200px; height: 769px; overflow: hidden; }
  body {
    background: var(--bg);
    font-family: "Open Sans", Arial, sans-serif;
    color: var(--text);
  }
  .spread {
    position: absolute;
    left: 20px;
    top: 174px;
    width: 1160px;
    height: 420px;
    display: flex;
    box-shadow: 0 10px 30px rgba(0,0,0,0.18);
  }
  .page {
    position: relative;
    width: 580px;
    height: 420px;
    background: var(--paper);
    overflow: hidden;
  }
  .page--left { border-right: 1px solid #e4e4e4; }
  .page-band {
    position: absolute;
    left: 0; top: 0;
    width: 580px; height: 52px;
  }
  .page-number {
    position: absolute;
    top: 8px; right: 18px;
    font-size: 9px;
    color: #ffffff;
    letter-spacing: 0.5px;
  }
  .skyline {
    position: absolute;
    left: 0; right: 0; bottom: 0;
    height: 120px;
    background: linear-gradient(to top, var(--skyline-dark) 0%, #a9abae 35%, var(--skyline-light) 75%, rgba(255,255,255,0) 100%);
    opacity: 0.75;
  }
  .page-content {
    position: relative;
    padding: 62px 34px 0 32px;
  }
  .section-title {
    font-size: 17px;
    font-weight: 600;
    color: var(--heading);
    line-height: 1.2;
    margin: 10px 0 6px;
  }
  .section-title:first-child { margin-top: 0; }
  .body-text {
    font-size: 10px;
    line-height: 1.4;
    margin-bottom: 6px;
  }
  .point-list {
    list-style: none;
    counter-reset: point;
    margin-bottom: 6px;
  }
  .point-list li {
    counter-increment: point;
    position: relative;
    padding-left: 16px;
    font-size: 10px;
    line-height: 1.4;
    margin-bottom: 1px;
  }
  .point-list li::before {
    content: counter(point) ".";
    position: absolute;
    left: 0;
    font-weight: 600;
    color: var(--heading);
  }
</style>
</head>
<body>
  <div class="spread">
    <section class="page page--left">
      <svg class="page-band" viewBox="0 0 580 52" aria-hidden="true">
        <defs>
          <linearGradient id="bandLeft" x1="0" y1="0" x2="1" y2="0">
            <stop offset="0" stop-color="#1c66a8"/>
            <stop offset="0.55" stop-color="#2b82c4"/>
            <stop offset="1" stop-color="#63b3e0"/>
          </linearGradient>
        </defs>
        <path d="M0 0 H580 V26 H260 L242 40 H0 Z" fill="url(#bandLeft)"/>
      </svg>
      <span class="page-number">08</span>
      <div class="skyline" role="img" aria-label="Graue Stadtsilhouette mit Hochhäusern am unteren Seitenrand"></div>
      <div class="page-content">
        <h2 class="section-title">Ist der Makler sein Geld wert?</h2>
        <p class="body-text">Wie bei jeder Dienstleistung, die Sie brauchen, wie Maler, Steuerberater, Installateur, Reinigungsfachkraft fragen Sie sich natürlich: Kann ich es nicht auch selber machen? Und selbstverständlich müssen Sie die Vor- und Nachteile abwägen, denn unsere Dienstleistung kostet natürlich Geld.</p>
        <h2 class="section-title">Warum erzielt ein Makler einen höheren Preis und ist schneller?</h2>
        <p class="body-text">Eine einfache Rechnung: Je mehr qualifizierte Interessenten, desto höher der Preis, je mehr Werbung/Marketing/Kundenstamm/Netzwerke desto mehr Interessenten.</p>
        <ol class="point-list">
          <li>Je realistischer der Angebotspreis, desto mehr Interessenten, je besser die Wertermittlung des realistischer der Angebotspreis, je mehr Bewertungsquellen, desto besser die Wertermittlung.</li>
          <li>Der Makler fängt nicht bei Punkt Null an, sondern hat bereits Interessenten.</li>
          <li>Einholung der Unterlagen, Erstellung Exposé, Anzeigenbuchung – hier hat der Makler Erfahrung. Eingespielte Abläufe, ihm entgeht kein Interessent, weil er im Urlaub ist oder bei Sport, denn die ständige Erreichbarkeit ist zu 100 % optimiert.</li>
        </ol>
      </div>
    </section>

    <section class="page page--right">
      <svg class="page-band" viewBox="0 0 580 52" aria-hidden="true">
        <defs>
          <linearGradient id="bandRight" x1="0" y1="0" x2="1" y2="0">
            <stop offset="0" stop-color="#1c66a8"/>
            <stop offset="0.55" stop-color="#2b82c4"/>
            <stop offset="1" stop-color="#63b3e0"/>
          </linearGradient>
        </defs>
        <path d="M0 0 H580 V26 H260 L242 40 H0 Z" fill="url(#bandRight)"/>
      </svg>
      <span class="page-number">09</span>
      <div class="skyline" role="img" aria-label="Graue Stadtsilhouette mit Hochhäusern am unteren Seitenrand"></div>
      <div class="page-content">
        <h2 class="section-title">Warum sind Sie entspannter und schonen Ihre Nerven wenn Sie eine Makler beauftragen?</h2>
        <ol class="point-list">
          <li>Die ersten 2 Interessenten sind zu dem vereinbarten Termin nicht gekommen - der Makler hat meist ein dickeres Fell als der Eigentümer und begrüßt auch den dritten Interessenten mit unverminderter guter Laune.</li>
          <li>Sie sind sich unsicher und wissen nicht was Sie dem Käufer erzählen müssen und was nicht!</li>
          <li>Sie fürchten Haftungsrisiken und juristische Fehler beim Verkauf?</li>
        </ol>
        <p class="body-text">Warum bevorzugen Interessenten einen Makler?</p>
        <ol class="point-list">
          <li>Sie wissen, dass der Makler ein Fachmann ist, der keine wesentlichen Mängel verschweigt.</li>
          <li>Sie wissen, dass Sie dem Makler Ihre Meinung sagen können, denn er ist nicht emotional befangen.</li>
          <li>Sie wissen, dass der Makler für seine Fehler haftet und diesbezüglich auch abgesichert ist.</li>
        </ol>
        <h2 class="section-title">Makler oder Bank beauftragen?</h2>
        <ol class="point-list">
          <li>Die Bank wird den Käufer bevorzugen, der bei ihr finanziert, nicht den, der den höchsten Kaufpreis bietet, denn mit der Finanzierung wird auch Geld verdient.</li>
          <li>Geben Sie sich bei der Bank mal als Kaufinteressent aus und versuchen Sie am Samstag oder Sonntag einen Termin zu bekommen – ein Banker lebt vom Gehalt, der Makler vom Erfolg.</li>
        </ol>
      </div>
    </section>
  </div>
</body>
</html>
```